Banner Ads & Design

We need banner ads for our affiliate marketing. Publishers who send us consumer traffic will put these banners on their websites to promote us. Our websites we will be promoting with the banners are: auto.tallbirchplace.com, home.tallbirchplace.com, life.tallbirchplace.com, health.tallbirchplace.com, medicare.tallbirchplace.com, autoclicks.tallbirchplace.com, lifeclicks.tallbirchplace.com, homeclicks.tallbirchplace.com

Target Market(s)

Consumers looking for insurance quotes in the United States

Industry/Entity Type

Insurance

Requirements
Must have
• Insurance themed. Consumer friendly. Project that their information they enter is safe and secure.

```html
<!DOCTYPE html>
<html lang="en">
<head>
<meta charset="utf-8">
<title>Life Insurance Quote Banners</title>
<link rel="stylesheet" href="https://fonts.googleapis.com/css2?family=Open+Sans:wdth,wght@75..100,300..800&display=swap">
<style>
  :root {
    --purple: #3d0066;
    --white: #ffffff;
    --ink: #3a3a3a;
    --photo-light: #eef1f4;
    --photo-mid: #c9b2a4;
    --photo-deep: #7f8a92;
    --shadow: rgba(0,0,0,0.35);
  }
  * { margin: 0; padding: 0; box-sizing: border-box; }
  html, body { width: 927px; height: 1200px; overflow: hidden; background: var(--white); }
  body { position: relative; font-family: "Open Sans", Arial, sans-serif; }

  .banner { position: absolute; background: var(--white); box-shadow: 0 3px 10px var(--shadow); overflow: hidden; }
  .banner svg.shape { position: absolute; left: 0; top: 0; }
  .headline { position: absolute; color: var(--white); font-weight: 700; text-transform: uppercase; white-space: nowrap; font-stretch: 75%; }
  .headline span { display: block; }
  .photo { position: absolute; background: radial-gradient(ellipse at 60% 55%, var(--photo-mid) 0%, var(--photo-deep) 45%, var(--photo-light) 80%); }
  .cta { position: absolute; background: var(--purple); color: var(--white); display: flex; align-items: center; justify-content: center; gap: 6px; font-weight: 500; font-stretch: 85%; text-transform: uppercase; white-space: nowrap; }
  .cta svg { flex: none; }
  .tagline { position: absolute; font-weight: 300; font-stretch: 75%; text-align: center; white-space: nowrap; }

  /* Leaderboard */
  .leaderboard { left: 36px; top: 56px; width: 868px; height: 107px; }
  .leaderboard .headline { left: 36px; top: 17px; font-size: 32px; line-height: 36px; font-stretch: 87%; }
  .leaderboard .tagline { left: 455px; top: 14px; width: 275px; color: var(--ink); font-size: 19.5px; line-height: 22px; }
  .leaderboard .cta { left: 520px; top: 65px; width: 130px; height: 31px; font-size: 16px; }
  .leaderboard .photo { left: 732px; top: 3px; width: 112px; height: 104px; }

  /* Skyscraper */
  .skyscraper { left: 68px; top: 208px; width: 241px; height: 902px; }
  .skyscraper .headline { left: 0; width: 241px; top: 37px; text-align: center; }
  .skyscraper .l1 { font-size: 58px; line-height: 54px; font-stretch: 86%; }
  .skyscraper .l2 { font-size: 51px; line-height: 50px; }
  .skyscraper .l3 { font-size: 37px; line-height: 40px; }
  .skyscraper .l4 { font-size: 80px; line-height: 74px; font-stretch: 81%; }
  .skyscraper .tagline { left: 0; width: 241px; top: 278px; color: var(--white); font-size: 23px; line-height: 31px; }
  .skyscraper .cta { left: 30px; top: 500px; width: 179px; height: 46px; font-size: 20px; }
  .skyscraper .photo { left: 2px; top: 580px; width: 238px; height: 216px; }
  .brand { position: absolute; left: 20px; top: 822px; display: flex; align-items: center; gap: 8px; color: var(--purple); font-weight: 700; font-stretch: 85%; font-size: 21px; }
  .brand i { width: 36px; height: 36px; border-radius: 50%; background: var(--purple); display: block; }

  /* Rectangle */
  .rectangle { left: 381px; top: 238px; width: 505px; height: 421px; }
  .rectangle .photo { left: 183px; top: 144px; width: 314px; height: 275px; }
  .rectangle .headline { left: 28px; top: 20px; }
  .rectangle .l1 { font-size: 50px; line-height: 46px; font-stretch: 97%; }
  .rectangle .l2 { font-size: 41px; line-height: 40px; font-stretch: 91%; }
  .rectangle .l3 { font-size: 33px; line-height: 36px; font-stretch: 81%; }
  .rectangle .l4 { font-size: 65px; line-height: 62px; font-stretch: 98%; }
  .rectangle .cta { left: 19px; top: 351px; width: 164px; height: 46px; font-size: 20px; }
</style>
</head>
<body>

<section class="banner leaderboard">
  <div class="photo" role="img" aria-label="Smiling family of four lying stacked together"></div>
  <svg class="shape" width="470" height="107" viewBox="0 0 470 107" aria-hidden="true">
    <path fill="var(--purple)" d="M0 0 H412 C432 6 402 30 420 48 C436 60 402 82 420 100 L412 107 H0 Z"/>
  </svg>
  <h2 class="headline"><span>Get Free &nbsp;Quotes On</span><span>Life Insurance &nbsp;Today</span></h2>
  <p class="tagline">We’ve helped people just like you find the<br>best insurance policy</p>
  <a class="cta"><svg width="9" height="14" viewBox="0 0 9 14"><path d="M1 1 L7 7 L1 13" stroke="#fff" stroke-width="2" fill="none"/></svg>Lean More</a>
</section>

<section class="banner skyscraper">
  <svg class="shape" width="241" height="480" viewBox="0 0 241 480" aria-hidden="true">
    <path fill="var(--purple)" d="M0 0 H241 V443 C228 450 215 430 200 440 C186 450 180 472 165 468 C150 464 150 445 135 444 C118 444 116 470 100 467 C86 464 85 440 70 438 C55 436 52 458 40 457 C28 456 26 436 15 436 C8 436 4 440 0 443 Z"/>
  </svg>
  <h2 class="headline"><span class="l1">Get Free</span><span class="l2">Quotes On</span><span class="l3">Life Insurance</span><span class="l4">Today</span></h2>
  <p class="tagline">We’ve helped people just<br>like you find the best<br>insurance policy</p>
  <a class="cta"><svg width="11" height="18" viewBox="0 0 11 18"><path d="M1 1 L9 9 L1 17" stroke="#fff" stroke-width="2.4" fill="none"/></svg>Lean More</a>
  <div class="photo" role="img" aria-label="Smiling family of four lying stacked together"></div>
  <div class="brand"><i></i>TallBirchPlace.com</div>
</section>

<section class="banner rectangle">
  <div class="photo" role="img" aria-label="Smiling family of four lying stacked together"></div>
  <svg class="shape" width="505" height="421" viewBox="0 0 505 421" aria-hidden="true">
    <path fill="var(--purple)" d="M0 0 H330 C318 10 346 20 342 32 C334 46 318 50 334 70 C346 86 318 96 322 112 C326 126 300 130 305 146 C310 164 286 170 276 180 C262 190 252 184 246 200 C240 216 222 214 210 226 C200 236 196 260 180 256 C166 252 166 238 150 246 C136 254 132 276 116 272 C100 268 98 250 82 258 C66 266 62 282 46 274 C32 266 26 254 14 262 C6 268 2 270 0 266 Z"/>
  </svg>
  <h2 class="headline"><span class="l1">Get Free</span><span class="l2">Quotes On</span><span class="l3">Life Insurance</span><span class="l4">Today</span></h2>
  <a class="cta"><svg width="11" height="18" viewBox="0 0 11 18"><path d="M1 1 L9 9 L1 17" stroke="#fff" stroke-width="2.4" fill="none"/></svg>Lean More</a>
</section>

</body>
</html>
```